willowcreekrestoring - healing business promotion

I have and energy / intuitive healing and kinesiology business. working with people who are looking for healing outside of the modern medical model, who have tried but failed in their search for understanding their conditions and why health and or happiness eludes them. the healing is done with love, patience and understanding. I am looking to be taken seriously with my presentation and to reach a person who may be deterred by the thought of angels and intuition! but to not exclude those that are attracted to that also.

Industry/Entity Type

Medical

Contact Information for Business Card

willowcreekrestoring
calm kind true energy balance practice
tamsin louise harte
energy healing / kinesiology and neurotraining
0417266183 07 4158 2746
home visits available for Marlow and Fernvale
t.lharte@quillmail.com

Requirements
Should not have
• Primary colours

```html
<!DOCTYPE html>
<html lang="en">
<head>
<meta charset="utf-8">
<title>Willow Creek Restoring – Business Card</title>
<link rel="stylesheet" href="https://fonts.googleapis.com/css2?family=Mulish:ital,wght@0,400;0,700;1,400&display=swap">
<style>
  :root {
    --leaf-dark: #4a7a2c;
    --leaf-deep: #3f6a25;
    --band-green: #97ec46;
    --mist-green: #cdf6a3;
    --mist-pale: #eafcd8;
    --white: #ffffff;
  }
  * { margin: 0; padding: 0; box-sizing: border-box; }
  html, body {
    width: 1200px;
    height: 741px;
    overflow: hidden;
    background: var(--white);
  }
  .card {
    position: relative;
    width: 1200px;
    height: 741px;
    overflow: hidden;
    font-family: "Mulish", sans-serif;
  }
  .card__backdrop {
    position: absolute;
    inset: 0;
    background:
      radial-gradient(ellipse 420px 260px at 1080px 40px, var(--mist-pale), transparent 70%),
      radial-gradient(ellipse 480px 240px at 120px 700px, var(--mist-pale), transparent 70%),
      radial-gradient(ellipse 360px 260px at 220px 60px, #dff9c4, transparent 70%),
      linear-gradient(160deg, var(--mist-green) 0%, #bff287 50%, var(--mist-green) 100%);
  }
  .card__band {
    position: absolute;
    inset: 0;
    width: 1200px;
    height: 741px;
  }
  .brand {
    position: absolute;
    left: 66px;
    top: 126px;
    display: flex;
    align-items: center;
    gap: 22px;
  }
  .brand__dot {
    width: 134px;
    height: 134px;
    border-radius: 50%;
    background: var(--leaf-dark);
    flex: none;
  }
  .brand__name {
    font-weight: 400;
    font-size: 56px;
    color: var(--leaf-dark);
    letter-spacing: 0.5px;
    white-space: nowrap;
  }
  .tagline {
    position: absolute;
    left: 248px;
    top: 238px;
    font-size: 29px;
    font-weight: 400;
    color: var(--white);
    letter-spacing: 2.2px;
    white-space: nowrap;
  }
  .contact {
    position: absolute;
    left: 541px;
    top: 362px;
  }
  .contact__name {
    font-size: 38px;
    font-weight: 400;
    color: var(--leaf-deep);
    letter-spacing: 0.6px;
    line-height: 1;
  }
  .contact__role {
    margin-top: 18px;
    font-size: 25px;
    color: var(--white);
    letter-spacing: 0.3px;
  }
  .contact__row {
    display: flex;
    align-items: center;
    gap: 12px;
    color: var(--leaf-deep);
  }
  .contact__row--phone {
    margin-top: 12px;
    font-weight: 700;
    font-size: 29px;
    letter-spacing: 0.4px;
  }
  .contact__row--mail {
    margin-top: 8px;
    font-size: 25px;
  }
  .contact__icon { width: 34px; height: 34px; flex: none; }
  .contact__note {
    margin-top: 14px;
    font-style: italic;
    font-size: 21.5px;
    color: var(--white);
    letter-spacing: 0.3px;
  }
</style>
</head>
<body>
  <main class="card">
    <div class="card__backdrop" role="img" aria-label="Soft pale green bokeh background with delicate glowing blossoms in the corners"></div>

    <svg class="card__band" viewBox="0 0 1200 741" aria-hidden="true">
      <defs>
        <linearGradient id="bandFill" x1="0" y1="0" x2="1" y2="0">
          <stop offset="0" stop-color="#a6ef60"/>
          <stop offset="0.5" stop-color="#97ec46"/>
          <stop offset="1" stop-color="#9cee4e"/>
        </linearGradient>
      </defs>
      <path d="M0,165 C320,162 560,58 880,62 C1040,64 1140,40 1200,22 L1200,668 C1020,640 860,598 700,604 C500,612 300,636 0,612 Z" fill="url(#bandFill)"/>
      <path d="M0,148 C320,146 560,42 880,46 C1040,48 1140,24 1200,6" fill="none" stroke="#ffffff" stroke-width="10" stroke-opacity="0.9"/>
      <path d="M0,630 C300,654 500,630 700,622 C860,616 1020,658 1200,686" fill="none" stroke="#ffffff" stroke-width="12" stroke-opacity="0.9"/>
    </svg>

    <div class="brand">
      <span class="brand__dot"></span>
      <span class="brand__name">Willow Creek Restoring</span>
    </div>
    <p class="tagline">calm kind true energy balance practice</p>

    <section class="contact">
      <h1 class="contact__name">Tamsin Louise Harte</h1>
      <p class="contact__role">Energy Healing / Kinesiology &amp; Neurotraining</p>
      <p class="contact__row contact__row--phone">
        <svg class="contact__icon" viewBox="0 0 34 34" aria-hidden="true">
          <rect x="1" y="1" width="32" height="32" rx="6" fill="#eafcd8"/>
          <path d="M12 8 c-3 1 -3 6 0 11 c3 5 7 8 10 7 l1.5 -3 l-4 -3 l-2 1.5 c-2 -1 -4 -4 -4.5 -6 l2 -1.5 l-1 -5 z" fill="#4a7a2c"/>
        </svg>
        <span>0417266183 07 4158 2746</span>
      </p>
      <p class="contact__row contact__row--mail">
        <svg class="contact__icon" viewBox="0 0 34 34" aria-hidden="true">
          <rect x="3" y="8" width="28" height="19" fill="none" stroke="#eafcd8" stroke-width="2"/>
          <path d="M3 8 L17 19 L31 8 M3 27 L13 16 M31 27 L21 16" fill="none" stroke="#eafcd8" stroke-width="2"/>
        </svg>
        <span>t.lharte@quillmail.com</span>
      </p>
      <p class="contact__note">Home visits available for Marlow and Fernvale</p>
    </section>
  </main>
</body>
</html>
```